Brochure for 2015 workshops

Looking for a brochure for Tip Top Tin Drum ,2015 professional development workshops. We are a creative consulting company for early childhood and looking at getting the brochure designed in a fun, recyclable and quirky design.I have attached all information needed to be included into the brochure as well as our logo.

Industry/Entity Type

It Company

```html
<!DOCTYPE html>
<html lang="en">
<head>
<meta charset="utf-8">
<title>Tip Top Tin Drum – Professional Development Workshops 2015</title>
<link href="https://fonts.googleapis.com/css2?family=Comic+Neue:wght@400;700&family=Lato:wght@400;700&display=swap" rel="stylesheet">
<style>
:root{
  --bg:#e9e6e1;
  --yellow:#f7e600;
  --lime:#9ccc1c;
  --green:#5fae19;
  --blue:#1a8fe6;
  --sky:#29a6f0;
  --navy:#1c5aa8;
  --orange:#f07a10;
  --orange-dk:#e65a0c;
  --amber:#ffb000;
  --ink:#222;
  --white:#fff;
}
*{box-sizing:border-box;margin:0;padding:0}
html,body{width:900px;height:1200px;overflow:hidden;background:var(--bg)}
body{position:relative;font-family:'Lato',sans-serif;color:var(--ink)}
.sheet{position:absolute;left:45px;width:810px;height:560px;display:flex;box-shadow:0 6px 18px rgba(0,0,0,.25)}
.sheet--front{top:30px}
.sheet--back{top:610px}
.panel{position:relative;width:270px;height:100%;overflow:hidden}
.wave{position:absolute;left:0;width:100%}
.heading,.tab,.pill,.display{font-family:'Comic Neue',sans-serif;font-weight:700}
.tab{position:relative;display:inline-block;background:var(--blue);color:var(--white);font-size:15px;padding:4px 18px 4px 14px;border-radius:0 14px 14px 0;margin-left:-14px}
.body{font-size:9px;line-height:1.35}
.body p{margin-bottom:4px}
.info{font-size:9.5px;line-height:1.4}
.info .label{font-family:'Comic Neue',sans-serif;font-weight:700;font-size:13px}
.pill{display:block;text-align:center;border-radius:16px;font-size:13px;padding:6px 0}
.content{position:absolute;left:14px;right:12px}

/* front */
.p-outdoor{background:linear-gradient(160deg,var(--yellow) 40%,#c9dd12)}
.p-outdoor .topics{list-style:none;font-size:9px;line-height:1.3;margin:8px 0 0}
.p-outdoor .topics li{position:relative;padding-left:12px;margin-bottom:6px}
.p-outdoor .topics li:before{content:"";position:absolute;left:2px;top:4px;width:5px;height:5px;border-radius:50%;background:var(--navy)}
.p-outdoor .info{color:var(--navy)}
.p-outdoor .info .label{color:var(--orange)}
.tea{width:165px;margin:10px auto 0;background:var(--orange-dk);color:var(--yellow);font-size:17px;line-height:1.15;border-radius:18px;padding:5px 0;text-align:center;box-shadow:0 3px 4px rgba(0,0,0,.25)}
.tea span{color:var(--white)}
.url-blue{position:absolute;left:22px;right:22px;bottom:20px;background:var(--sky);color:var(--white);box-shadow:0 2px 3px rgba(0,0,0,.25)}

.p-sandman{background:linear-gradient(180deg,var(--sky),#1178d8)}
.p-sandman .heading{font-size:15px;color:var(--ink);margin-bottom:8px}
.p-sandman .body{color:#e6f4ff}
.session-box{position:absolute;left:-6px;top:216px;width:180px;background:var(--orange-dk);border-radius:0 10px 10px 0;padding:10px 14px 12px 20px;box-shadow:0 4px 6px rgba(0,0,0,.3)}
.session-box .title{font-family:'Comic Neue',sans-serif;font-weight:700;color:var(--white);font-size:19px;line-height:1}
.session-box .title small{display:block;font-size:15px}
.session-box .details{font-family:'Comic Neue',sans-serif;font-weight:700;color:var(--yellow);font-size:14px;line-height:1.15;margin-top:8px}
.session-box .details b{color:var(--white)}
.venue{position:absolute;left:0;right:0;top:410px;text-align:center;color:var(--white)}
.venue .heading{font-size:24px;color:var(--yellow);display:flex;align-items:center;justify-content:center;gap:8px}
.venue .heading:before,.venue .heading:after{content:"";width:40px;height:1px;background:var(--white)}
.venue p{font-family:'Comic Neue',sans-serif;font-weight:700;font-size:11.5px;line-height:1.3;margin-top:6px}
.url-yellow{position:absolute;left:14px;right:14px;bottom:20px;background:var(--yellow);color:var(--navy)}

.p-cover{background:var(--green)}
.cover-top{position:absolute;left:0;right:0;top:0;height:320px;background:linear-gradient(180deg,var(--orange) 0%,var(--amber) 70%)}
.display{position:absolute;left:22px;top:48px;font-size:34px;line-height:1.12}
.display .l1{color:var(--navy)}
.display .l2{color:var(--green)}
.display .l3{color:var(--navy)}
.display .l4{color:#111;font-size:41px}
.brand{position:absolute;left:55px;top:420px;display:flex;align-items:center;gap:8px;font-family:'Comic Neue',sans-serif;font-weight:700;font-size:17px;color:#3a2a1a}
.brand i{display:block;width:14px;height:14px;background:#3a2a1a}
.brand-tag{position:absolute;left:55px;top:444px;font-size:8px;color:var(--yellow)}
.url-orange{position:absolute;left:16px;right:16px;bottom:20px;background:var(--orange-dk);color:var(--white);box-shadow:0 2px 3px rgba(0,0,0,.25)}

/* back */
.p-white{background:var(--white)}
.p-green{background:linear-gradient(180deg,#6ab51b,var(--lime))}
.p-white .tab{background:var(--blue)}
.presenter{font-family:'Comic Neue',sans-serif;font-weight:700;font-size:12px;color:var(--orange);margin:8px 0 2px}
.p-white .info{color:var(--navy);font-size:9px}
.p-green .heading{font-size:14px;color:var(--white);border-bottom:1px solid var(--white);display:inline-block;padding-bottom:2px;margin-bottom:6px}
.p-green .body{color:#13331a}
.p-green .presenter{color:var(--yellow)}
.p-green .info{color:#fff6a0;font-size:9px}
.extras{font-family:'Comic Neue',sans-serif;font-weight:700;font-size:12px;color:var(--green);line-height:1.2;margin-top:8px}
.lunch{position:absolute;right:16px;bottom:22px;text-align:right;font-family:'Comic Neue',sans-serif;font-weight:700;font-size:14px;line-height:1.2;color:var(--yellow)}
</style>
</head>
<body>

<section class="sheet sheet--front">
  <article class="panel p-outdoor">
    <svg class="wave" style="top:0" viewBox="0 0 270 120" height="120" preserveAspectRatio="none" aria-hidden="true">
      <path d="M0 0H270V40C200 10 130 60 60 40 30 32 10 30 0 34Z" fill="#5fae19"/>
      <path d="M0 34C40 22 80 40 130 50 190 62 230 70 270 60V80C220 90 180 80 120 68 70 58 30 50 0 58Z" fill="#1c5aa8"/>
      <path d="M0 58C40 50 80 60 130 70 190 82 230 90 270 80V86C230 96 180 90 120 78 70 68 30 62 0 66Z" fill="#fff" opacity=".8"/>
    </svg>
    <div class="content" style="top:108px">
      <span class="tab">Out to Play</span>
      <p class="body" style="margin-top:14px">Three hour workshop offering practical solution in how to Re-invent the great outdoors.</p>
      <span class="tab" style="margin-top:10px">Topics covered are:</span>
      <ul class="topics">
        <li>Fixed layouts, how to work within your constants.</li>
        <li>Creating an outdoor play space on a budget</li>
        <li>Designing and implementing a natural play space</li>
        <li>Creating an inviting space for children self-discovery</li>
        <li>The joys of water play</li>
        <li>Mess is best.. Getting children back to basics.</li>
      </ul>
      <div class="info" style="margin-top:6px">
        <div class="label">WORKSHOP INFORMATION:</div>
        <div style="font-family:'Comic Neue',sans-serif;font-weight:700;font-size:11px">Tuesday 17th March</div>
        Morning session: 9:30am – 12:30pm<br>
        $60 per person per session<br>
        (Max: 20 people)<br>
        Phone: 0400 512 734<br>
        Email: dana.whitfield@tiptoptindrum.com.au
      </div>
      <div class="tea">Morning Tea<br><span>provided</span></div>
    </div>
    <span class="pill url-blue">www.tiptoptindrum.com.au</span>
  </article>

  <article class="panel p-sandman">
    <div class="content" style="top:14px">
      <h2 class="heading">Mr Sandman</h2>
      <div class="body">
        <p>Creative play in the humble sandpit has never been so interesting! So much more than a place to build castles, the sandpit presents an exciting opportunity for early childhood workers to unleash the teacher within!<br>There is no right way or wrong way to use sand...except maybe throwing it! Sandpits invite participation.</p>
        <p>Children's ideas are made and tested, their imaginations are stretched and they can be soothed by the sensory experience of digging in deep.</p>
        <p>So much sand, so much can be done, so much is to be gained from doing it!</p>
      </div>
    </div>
    <div class="session-box">
      <div class="title">WORKSHOP<small>INFORMATION:</small></div>
      <div class="details">Tuesday<br>17th March<br><b>Afternoon session:<br>1.00pm -4.00pm<br>$60 per person</b><br>per session<br>(Max: 20 people)</div>
    </div>
    <div class="venue">
      <div class="heading">Venue</div>
      <p>St Brigid's Parish Hall,<br>52 Elmwood Rd, Ashford North</p>
    </div>
    <span class="pill url-yellow">www.tiptoptindrum.com.au</span>
  </article>

  <article class="panel p-cover">
    <div class="cover-top"></div>
    <svg class="wave" style="top:290px" viewBox="0 0 270 70" height="70" preserveAspectRatio="none" aria-hidden="true">
      <path d="M0 0C40 40 120 50 180 30 220 18 250 10 270 8V70H0Z" fill="#1c5aa8"/>
      <path d="M0 12C50 50 120 58 180 40 220 28 250 22 270 20V70H0Z" fill="#fff"/>
      <path d="M0 24C50 62 120 66 180 52 220 42 250 36 270 34V70H0Z" fill="#5fae19"/>
    </svg>
    <h1 class="display"><span class="l1">Professional</span><br><span class="l2">Development</span><br><span class="l3">Workshops</span><br><span class="l4">for 2015</span></h1>
    <div class="brand"><i></i>Tip Top Tin Drum</div>
    <div class="brand-tag">creative consulting for early childhood</div>
    <span class="pill url-orange">www.tiptoptindrum.com.au</span>
  </article>
</section>

<section class="sheet sheet--back">
  <article class="panel p-white">
    <svg class="wave" style="top:0" viewBox="0 0 270 80" height="80" preserveAspectRatio="none" aria-hidden="true">
      <path d="M0 0H270V20C200 0 120 10 60 30 30 40 10 46 0 50Z" fill="#1a8fe6"/>
      <path d="M0 50C50 26 120 20 180 36 220 46 250 54 270 52V64C240 70 200 60 160 50 100 36 50 44 0 60Z" fill="#f07a10"/>
    </svg>
    <div class="content" style="top:54px">
      <span class="tab">You and I</span>
      <p class="body" style="margin-top:10px">Do you know what your working style is?<br>Do you know how you are perceived in the workplace? The more you are aware of your own traits and working styles the better you can adapt when required. This session looks at examining work styles and looking at how different styles interact.</p>
      <div class="presenter">Presenter: Rosa Kendrick</div>
      <div class="info">Wednesday 11th March 2015<br>9:30-12.30<br>Duration: 3 hours<br>$60 per person.<br>per session (Max: 20 people)<br>Phone 0400 512 734<br>Email: dana.whitfield@tiptoptindrum.com.au</div>
      <span class="tab" style="margin-top:14px">Argy Bargy / Playing Nicely</span>
      <p class="body" style="margin-top:10px">Sometimes working with different people is easy and you just click, sometimes it is more challenging. Working in teams can be incredibly rewarding provided you can navigate the different dynamics.<br>This session examines group theory and what defines a successful team and how to manage conflict.</p>
      <div class="presenter">Presenter: Rosa Kendrick</div>
      <div class="info">Wednesday 11th February<br>9:30am – 12:30pm<br>Duration: 3 hours<br>$60 per person.<br>per session (Max: 20 people)<br>Phone: 0400 512 734<br>Email: dana.whitfield@tiptoptindrum.com.au</div>
    </div>
  </article>

  <article class="panel p-green">
    <div class="content" style="top:16px">
      <h2 class="heading">Looking in the mirror</h2>
      <p class="body">There is a lot of talk about the value of reflective practices? Do you know what this means? Do you know how to truly reflect on both your practices and your programming?<br>Looking in the mirror gives you practical advice and exercises that will assist in your reflective practices. This session will take you beyond the stock standard techniques and also demonstrate how to clearly make the leap from reflective practices to improved performance.</p>
      <div class="presenter">Presenter: Rosa Kendrick</div>
      <div class="info">Wednesday 8th April<br>9:30am – 12:30pm<br>Duration: 3 hours<br>$60 per person.<br>per session (Max: 20 people)<br>Phone: 0400 512 734<br>Email: dana.whitfield@tiptoptindrum.com.au</div>
      <h2 class="heading" style="margin-top:14px">Critique Mystique</h2>
      <p class="body">Conducting staff appraisals that are meaningful and get results can be both daunting and incredibly time consuming.<br>Critique Mystique will take the mystery out of performance reviews and give you templates and techniques that can assist you conduct staff reviews confidently and competently<br>Part of this session will also give you the opportunity to practice giving both positive and negative feedback.</p>
      <div class="presenter">Presenter: Dana Whitfield</div>
      <div class="info">Date: Wednesday 8th April<br>Time: 1.00 - 4.00pm<br>Duration: 3 hours<br>Price: $60 per person. per session<br>(Max: 20 people)<br>Phone: 0400 512 734<br>Email: dana.whitfield@tiptoptindrum.com.au</div>
    </div>
  </article>

  <article class="panel p-white">
    <div class="content" style="top:26px">
      <span class="tab">Recycle, Reuse, Reimagine</span>
      <p class="body" style="margin-top:12px">In the hands of a child, a piece of bumpy foam becomes the surface of the moon, a milk bottle becomes a picnic basket and a bucket filled with plastic bottle tops becomes a snake or a necklace or maybe a mosaic mural. In this workshop we play with ideas, explore materials and discover how recycling and reusing can infiltrate your entire program!</p>
      <div class="presenter">Presenter: Joanne Hale</div>
      <div class="info">Tuesday 17th February<br>Tuesday 21st April<br>9:30 am – 12:30pm<br>Duration: 3 hours<br>Price: $60 per person. per session<br>(Max: 20 people)<br>Phone 0400 512 734<br>Email: dana.whitfield@tiptoptindrum.com.au<br>Register by Friday 13th Feb<br>Friday 10th April</div>
      <span class="tab" style="margin-top:14px">Don't Stress the Mess</span>
      <p class="body" style="margin-top:10px">Messy play delights the senses. When you're a child, a bowl of jelly is not just a bowl of jelly; it is a dinosaur land, an alien's slime and a fairy's bouncy castle. Early childhood educators don't need to stress about the mess of messy play. This hands-on workshop will explain why mess is vital in an early childhood setting and how to enjoy it!</p>
      <div class="extras">Morning &amp; Afternoon<br>Tea provided</div>
    </div>
    <svg class="wave" style="bottom:0" viewBox="0 0 270 100" height="100" preserveAspectRatio="none" aria-hidden="true">
      <path d="M0 30C60 10 140 0 200 10 230 16 255 24 270 20V100H0Z" fill="#f07a10"/>
      <path d="M0 40C60 20 140 12 200 22 230 28 255 34 270 32V100H0Z" fill="#1a8fe6"/>
    </svg>
    <div class="lunch">Lunch provided for<br>full day participants</div>
  </article>
</section>

</body>
</html>
```